Catalog for our Gold Coins for high value market

We need someone who makes our catalog or book for the gold coins of Switzerland.
Please use the Word Document. The text and the images are below. Feel free to make a nice design. Also make a nice design as a title.
Please use Adobe Indesign or Illustrator to make the content adjustable for us if needed.

You could also add a "star rating" from 1-4 for some of the coins with an image. I will do the rating later. It should be a rating of how precious the coins are without entering a price.
You could also adjust the title design with the coins.

Please make at least the following pages:
Title
Table of content
Title Page for each Ares (Aargau Page 6, Appenzell Page 6, Basel Page 8 and so on)
Pages with the content (Coins including the description)

Target Market(s)

Gold coins collectors. Usually those people are rich men.

Requirements
Must have
• Modern design
Should not have
• Not too many colors used. It should be modern. But have some class.

```html
<!DOCTYPE html>
<html lang="de">
<head>
<meta charset="utf-8">
<title>Goldmünzen der Kantone und Eidgenossenschaft – Katalog</title>
<link href="https://fonts.googleapis.com/css2?family=Montserrat:wght@400;500;600;700;800&display=swap" rel="stylesheet">
<style>
  :root{
    --red:#d3202f;
    --red-dark:#a5121f;
    --blue:#1f3f9a;
    --blue-dark:#142a6b;
    --white:#ffffff;
    --ink:#3a3a3a;
    --muted:#8a8a8a;
    --stage:#e4e4e4;
    --gold-light:#f6dc8a;
    --gold:#d9a93a;
    --gold-dark:#8f6512;
  }
  *{box-sizing:border-box;margin:0;padding:0}
  html,body{width:1200px;height:2664px;overflow:hidden}
  body{
    background:var(--stage);
    font-family:"Montserrat",sans-serif;
    color:var(--ink);
    display:flex;flex-direction:column;align-items:center;
    gap:48px;padding-top:40px;
  }
  .spread{display:flex;width:920px;height:600px}
  .page{position:relative;width:460px;height:600px;background:var(--white);overflow:hidden}
  .spread .page + .page{border-left:1px solid #d6d6d6}
  .wave{position:absolute;left:0;width:100%;display:block}

  .brand{display:flex;align-items:center;gap:8px;font-weight:800;font-size:15px;
    letter-spacing:.12em;color:var(--red);text-transform:uppercase}
  .brand-mark{width:12px;height:12px;background:var(--blue)}

  .coin{position:absolute;border-radius:50%;
    background:radial-gradient(circle at 35% 30%,var(--gold-light),var(--gold) 55%,var(--gold-dark));
    box-shadow:0 3px 6px rgba(0,0,0,.25)}

  /* Cover */
  .cover .brand{position:absolute;top:40px;left:50%;transform:translateX(-50%)}
  .cover-title{position:absolute;top:100px;width:100%;text-align:center}
  .cover-title h1{font-size:34px;font-weight:800;color:var(--red);line-height:1.1}
  .cover-title p{font-size:17px;font-weight:600;color:var(--blue);margin-top:6px;line-height:1.3}
  .cover-url{position:absolute;top:428px;width:100%;text-align:center;font-size:10px;
    color:var(--muted);letter-spacing:.05em}

  /* Back cover */
  .back{background:var(--red)}
  .back .brand-box{position:absolute;top:36px;left:40px;background:var(--white);padding:10px 14px}
  .contact{position:absolute;top:180px;left:40px;color:var(--white);list-style:none}
  .contact li{margin-bottom:16px}
  .contact .label{display:block;font-size:9px;font-weight:500;opacity:.8;letter-spacing:.06em;text-transform:uppercase}
  .contact .value{font-size:14px;font-weight:700;line-height:1.35}
  .back-url{position:absolute;bottom:60px;left:40px;color:var(--white);font-size:13px;font-weight:600}

  /* Front in spread */
  .front .brand{position:absolute;top:36px;right:36px}
  .front .cover-title{top:86px;left:auto;right:0;width:auto;padding-right:36px;text-align:right}
  .front .cover-title h1{font-size:30px}
  .front .cover-title p{font-size:15px}
  .front .cover-url{top:auto;bottom:22px;color:var(--white);z-index:2}

  /* Canton opener */
  .opener-photo{position:absolute;inset:0;
    background:radial-gradient(circle at 50% 60%,#c9a24a,#7d5a1c 55%,#3a2a10)}
  .opener-title{position:absolute;top:34px;left:34px;color:var(--white);z-index:2}
  .opener-title h2{font-size:34px;font-weight:800;letter-spacing:.08em}
  .opener-title p{font-size:10px;font-weight:500;margin-top:2px;opacity:.9}

  /* Content page */
  .content-head{position:absolute;top:40px;left:150px;z-index:2}
  .content-head h2{font-size:32px;font-weight:700;color:var(--blue)}
  .content-head p{font-size:10px;color:var(--red);font-weight:600;margin-top:2px}
  .coin-row{position:absolute;left:0;width:100%;display:flex;justify-content:center;gap:50px}
  .coin-item{display:flex;flex-direction:column;align-items:center;gap:8px}
  .coin-item .coin{position:static}
  .stars{display:flex;gap:3px}
  .stars svg{width:11px;height:11px}
  .caption{font-size:9px;color:var(--muted);font-weight:500}
  .page-no{position:absolute;bottom:20px;right:28px;font-size:9px;color:var(--muted)}
</style>
</head>
<body>

<svg width="0" height="0" style="position:absolute">
  <defs>
    <symbol id="star" viewBox="0 0 24 24"><path d="M12 2l3 6.9 7.4.7-5.6 4.9 1.7 7.3L12 18l-6.5 3.8 1.7-7.3L1.6 9.6 9 8.9z"/></symbol>
  </defs>
</svg>

<!-- Cover -->
<section class="page cover">
  <div class="brand"><span class="brand-mark"></span>Aurum Keller</div>
  <div class="cover-title">
    <h1>Goldmünzen</h1>
    <p>der Kantone und<br>Eidgenossenschaft</p>
  </div>
  <div role="img" aria-label="Arrangement of five Swiss gold coins">
    <div class="coin" style="width:92px;height:92px;left:96px;top:218px"></div>
    <div class="coin" style="width:86px;height:86px;left:278px;top:214px"></div>
    <div class="coin" style="width:96px;height:96px;left:182px;top:288px"></div>
    <div class="coin" style="width:82px;height:82px;left:80px;top:326px"></div>
    <div class="coin" style="width:84px;height:84px;left:296px;top:320px"></div>
  </div>
  <p class="cover-url">www.aurum-keller.ch</p>
  <svg class="wave" style="bottom:0;height:160px" viewBox="0 0 460 160" preserveAspectRatio="none">
    <path d="M0 30 Q200 -10 460 26 L460 160 L0 160Z" fill="var(--blue)"/>
    <path d="M0 48 Q200 8 460 44 L460 160 L0 160Z" fill="var(--white)"/>
    <path d="M0 58 Q200 18 460 54 L460 160 L0 160Z" fill="var(--red)"/>
    <path d="M0 120 Q240 90 460 130 L460 160 L0 160Z" fill="var(--red-dark)" opacity=".5"/>
  </svg>
</section>

<!-- Back + front cover -->
<section class="spread">
  <div class="page back">
    <svg class="wave" style="top:0;height:150px" viewBox="0 0 460 150" preserveAspectRatio="none">
      <path d="M120 0 L460 0 L460 110 Q320 40 120 0Z" fill="var(--blue)"/>
      <path d="M0 0 L120 0 Q320 40 460 110 L460 122 Q300 56 0 14Z" fill="var(--white)" opacity=".9"/>
    </svg>
    <div class="brand-box"><div class="brand"><span class="brand-mark"></span>Aurum Keller</div></div>
    <ul class="contact">
      <li><span class="label">Telefon</span><span class="value">+41 (0)44 555 01 20</span></li>
      <li><span class="label">Fax</span><span class="value">+41 (0)44 555 01 21</span></li>
      <li><span class="label">E-Mail</span><span class="value">info@aurum-keller.ch</span></li>
      <li><span class="label">Adresse</span><span class="value">Musterweg 12, 8000 Beispielstadt<br>Switzerland</span></li>
    </ul>
    <p class="back-url">www.aurum-keller.ch</p>
  </div>
  <div class="page front">
    <div class="brand"><span class="brand-mark"></span>Aurum Keller</div>
    <div class="cover-title">
      <h1>Goldmünzen</h1>
      <p>der Kantone und<br>Eidgenossenschaft</p>
    </div>
    <div role="img" aria-label="Arrangement of five Swiss gold coins">
      <div class="coin" style="width:80px;height:80px;left:200px;top:200px"></div>
      <div class="coin" style="width:80px;height:80px;left:320px;top:196px"></div>
      <div class="coin" style="width:84px;height:84px;left:150px;top:290px"></div>
      <div class="coin" style="width:84px;height:84px;left:258px;top:286px"></div>
      <div class="coin" style="width:72px;height:72px;left:364px;top:296px"></div>
    </div>
    <svg class="wave" style="bottom:0;height:170px" viewBox="0 0 460 170" preserveAspectRatio="none">
      <path d="M0 40 Q220 -10 460 30 L460 170 L0 170Z" fill="var(--blue)"/>
      <path d="M0 58 Q220 8 460 48 L460 170 L0 170Z" fill="var(--white)"/>
      <path d="M0 68 Q220 18 460 58 L460 170 L0 170Z" fill="var(--red)"/>
    </svg>
    <p class="cover-url">www.aurum-keller.ch</p>
  </div>
</section>

<!-- Aargau -->
<section class="spread">
  <div class="page">
    <div class="opener-photo" role="img" aria-label="Close-up photograph of historic Aargau gold and silver coins"></div>
    <svg class="wave" style="top:0;height:150px" viewBox="0 0 460 150" preserveAspectRatio="none">
      <path d="M0 0 L460 0 L460 70 Q240 150 0 110Z" fill="var(--blue)"/>
      <path d="M0 0 L460 0 L460 58 Q240 134 0 96Z" fill="var(--white)"/>
      <path d="M0 0 L460 0 L460 50 Q240 124 0 88Z" fill="var(--red)"/>
    </svg>
    <div class="opener-title"><h2>AARGAU</h2><p>Goldmünzen des Kantons 1807 – 1813</p></div>
  </div>
  <div class="page">
    <svg class="wave" style="top:0;height:140px" viewBox="0 0 460 140" preserveAspectRatio="none">
      <path d="M0 0 L150 0 Q90 70 0 140Z" fill="var(--blue)"/>
      <path d="M0 0 L132 0 Q76 60 0 118Z" fill="var(--white)"/>
      <path d="M0 0 L124 0 Q70 54 0 108Z" fill="var(--red)"/>
    </svg>
    <div class="content-head"><h2>Aargau</h2><p>Goldmünzen des Kantons 1807 – 1813</p></div>
    <div class="coin-row" style="top:170px">
      <div class="coin-item">
        <div class="coin" role="img" aria-label="Aargau gold coin, obverse" style="width:100px;height:100px"></div>
        <div class="stars" style="fill:var(--gold)"><svg><use href="#star"/></svg><svg><use href="#star"/></svg><svg><use href="#star"/></svg><svg style="fill:#ddd"><use href="#star"/></svg></div>
        <span class="caption">8 Franken 1807</span>
      </div>
      <div class="coin-item">
        <div class="coin" role="img" aria-label="Aargau gold coin, reverse" style="width:100px;height:100px"></div>
        <div class="stars" style="fill:var(--gold)"><svg><use href="#star"/></svg><svg><use href="#star"/></svg><svg style="fill:#ddd"><use href="#star"/></svg><svg style="fill:#ddd"><use href="#star"/></svg></div>
        <span class="caption">4 Franken 1809</span>
      </div>
    </div>
    <div class="coin-row" style="top:350px">
      <div class="coin-item">
        <div class="coin" role="img" aria-label="Aargau gold coin" style="width:100px;height:100px"></div>
        <div class="stars" style="fill:var(--gold)"><svg><use href="#star"/></svg><svg><use href="#star"/></svg><svg><use href="#star"/></svg><svg><use href="#star"/></svg></div>
        <span class="caption">16 Franken 1813</span>
      </div>
      <div class="coin-item">
        <div class="coin" role="img" aria-label="Aargau gold coin" style="width:100px;height:100px"></div>
        <div class="stars" style="fill:var(--gold)"><svg><use href="#star"/></svg><svg><use href="#star"/></svg><svg style="fill:#ddd"><use href="#star"/></svg><svg style="fill:#ddd"><use href="#star"/></svg></div>
        <span class="caption">8 Franken 1813</span>
      </div>
    </div>
    <span class="page-no">7</span>
  </div>
</section>

<!-- Appenzell -->
<section class="spread">
  <div class="page">
    <div class="opener-photo" role="img" aria-label="Close-up photograph of historic Appenzell coins" style="background:radial-gradient(circle at 45% 55%,#b99a62,#6e5a3a 55%,#2e2418)"></div>
    <svg class="wave" style="top:0;height:150px" viewBox="0 0 460 150" preserveAspectRatio="none">
      <path d="M0 0 L460 0 L460 70 Q240 150 0 110Z" fill="var(--blue)"/>
      <path d="M0 0 L460 0 L460 58 Q240 134 0 96Z" fill="var(--white)"/>
      <path d="M0 0 L460 0 L460 50 Q240 124 0 88Z" fill="var(--red)"/>
    </svg>
    <div class="opener-title"><h2>APPENZELL</h2><p>Goldmünzen des Kantons 1737 – 1812</p></div>
  </div>
  <div class="page">
    <svg class="wave" style="top:0;height:140px" viewBox="0 0 460 140" preserveAspectRatio="none">
      <path d="M0 0 L150 0 Q90 70 0 140Z" fill="var(--blue)"/>
      <path d="M0 0 L132 0 Q76 60 0 118Z" fill="var(--white)"/>
      <path d="M0 0 L124 0 Q70 54 0 108Z" fill="var(--red)"/>
    </svg>
    <div class="content-head"><h2>Appenzell</h2><p>Goldmünzen des Kantons 1737 – 1812</p></div>
    <div class="coin-row" style="top:170px">
      <div class="coin-item">
        <div class="coin" role="img" aria-label="Appenzell gold coin, obverse" style="width:100px;height:100px"></div>
        <div class="stars" style="fill:var(--gold)"><svg><use href="#star"/></svg><svg><use href="#star"/></svg><svg><use href="#star"/></svg><svg style="fill:#ddd"><use href="#star"/></svg></div>
        <span class="caption">1 Dukat 1737</span>
      </div>
      <div class="coin-item">
        <div class="coin" role="img" aria-label="Appenzell gold coin, reverse" style="width:100px;height:100px"></div>
        <div class="stars" style="fill:var(--gold)"><svg><use href="#star"/></svg><svg><use href="#star"/></svg><svg style="fill:#ddd"><use href="#star"/></svg><svg style="fill:#ddd"><use href="#star"/></svg></div>
        <span class="caption">2 Dukat 1740</span>
      </div>
    </div>
    <div class="coin-row" style="top:350px">
      <div class="coin-item">
        <div class="coin" role="img" aria-label="Appenzell gold coin" style="width:100px;height:100px"></div>
        <div class="stars" style="fill:var(--gold)"><svg><use href="#star"/></svg><svg><use href="#star"/></svg><svg><use href="#star"/></svg><svg><use href="#star"/></svg></div>
        <span class="caption">4 Franken 1812</span>
      </div>
      <div class="coin-item">
        <div class="coin" role="img" aria-label="Appenzell gold coin" style="width:100px;height:100px"></div>
        <div class="stars" style="fill:var(--gold)"><svg><use href="#star"/></svg><svg><use href="#star"/></svg><svg><use href="#star"/></svg><svg style="fill:#ddd"><use href="#star"/></svg></div>
        <span class="caption">8 Franken 1812</span>
      </div>
    </div>
    <span class="page-no">9</span>
  </div>
</section>

</body>
</html>
```